property maintenance company covering all trades Plumbing,heating ,electrical building carpentry

business cards

Target Market(s)

DOMESTIC HOUSEHOLDS

Industry/Entity Type

Property Maintenance

Contact Information for Business Card

dorian Pellow
07815 390461
Bramwick Property Maintenace

Font styles to use
Sans Serif

Colors
eda3c7
d2a4cc
b7a5cd

```html
<!DOCTYPE html>
<html lang="en">
<head>
<meta charset="utf-8">
<title>Bramwick Property Maintenace – Business Cards</title>
<link rel="stylesheet" href="https://fonts.googleapis.com/css2?family=Montserrat:ital,wght@0,400;0,600;1,400&display=swap">
<style>
  :root {
    --stage: #1d1d1f;
    --card-dark: #2b2a2d;
    --card-dark-edge: #232225;
    --rose: #eda3c7;
    --orchid: #d2a4cc;
    --lavender: #b7a5cd;
    --white: #ffffff;
    --soft-text: #e6e1e8;
    --card-w: 520px;
    --card-h: 300px;
  }
  * { margin: 0; padding: 0; box-sizing: border-box; }
  html, body { width: 1200px; height: 873px; overflow: hidden; }
  body {
    background: var(--stage);
    display: flex;
    align-items: center;
    justify-content: center;
    gap: 60px;
    font-family: "Montserrat", sans-serif;
  }
  .card {
    position: relative;
    width: var(--card-w);
    height: var(--card-h);
    border-radius: 18px;
    overflow: hidden;
  }

  /* Front: dark card */
  .card--front {
    background: linear-gradient(135deg, #333236 0%, var(--card-dark) 45%, var(--card-dark-edge) 100%);
  }
  .card--front .texture {
    position: absolute; inset: 0;
    background: linear-gradient(160deg, rgba(255,255,255,0.05) 0%, rgba(0,0,0,0.08) 60%, rgba(255,255,255,0.03) 100%);
  }
  .brand {
    position: absolute;
    left: 24px; right: 24px;
    text-align: center;
  }
  .card--front .brand { top: 46px; }
  .brand__name {
    font-family: "Montserrat", sans-serif;
    font-weight: 600;
    font-size: 25px;
    line-height: 1.2;
    white-space: nowrap;
  }
  .card--front .brand__name { color: var(--rose); }
  .brand__trades {
    margin-top: 8px;
    font-weight: 400;
    font-size: 12.5px;
    letter-spacing: 0.4px;
    white-space: nowrap;
  }
  .card--front .brand__trades { color: var(--lavender); }

  .person {
    position: absolute;
    left: 60px;
    bottom: 56px;
    width: 180px;
    text-align: right;
  }
  .person__name {
    font-weight: 600;
    font-size: 19px;
    color: var(--orchid);
  }
  .person__role {
    font-style: italic;
    font-size: 12px;
    color: #d9d4dc;
    margin-top: 3px;
  }
  .divider {
    position: absolute;
    left: 262px;
    top: 150px;
    width: 1px;
    height: 110px;
    background: linear-gradient(180deg, transparent, var(--rose) 40%, var(--rose) 60%, transparent);
  }
  .contact {
    position: absolute;
    left: 290px;
    top: 176px;
    display: flex;
    align-items: center;
    gap: 12px;
    font-size: 15px;
    letter-spacing: 0.5px;
    color: var(--soft-text);
  }
  .contact__icon { width: 20px; height: 20px; fill: var(--orchid); }

  /* Back: pink card */
  .card--back {
    background: linear-gradient(135deg, var(--rose) 0%, #e39bc0 55%, var(--orchid) 100%);
  }
  .card--back .brand { top: 116px; }
  .card--back .brand__name { color: var(--white); }
  .card--back .brand__trades { color: var(--white); }
</style>
</head>
<body>
  <section class="card card--front" aria-label="Business card front">
    <div class="texture" role="img" aria-label="Faint low-poly faceted background pattern"></div>
    <div class="brand">
      <div class="brand__name">Bramwick Property Maintenace</div>
      <div class="brand__trades">Plumbing · Heating · Electrical · Building · Carpentry</div>
    </div>
    <div class="person">
      <div class="person__name">dorian Pellow</div>
      <div class="person__role">President</div>
    </div>
    <div class="divider"></div>
    <div class="contact">
      <svg class="contact__icon" viewBox="0 0 24 24" aria-hidden="true">
        <path d="M3 8c0-2 2-4 9-4s9 2 9 4v2h-5V8c-1-.6-2.4-1-4-1s-3 .4-4 1v2H3z"/>
        <path d="M6 12h12l2 8H4z M12 14a2.5 2.5 0 1 0 0 5a2.5 2.5 0 1 0 0-5z" fill-rule="evenodd"/>
      </svg>
      <span class="contact__phone">07815 390461</span>
    </div>
  </section>

  <section class="card card--back" aria-label="Business card back">
    <div class="brand">
      <div class="brand__name">Bramwick Property Maintenace</div>
      <div class="brand__trades">Plumbing · Heating · Electrical · Building · Carpentry</div>
    </div>
  </section>
</body>
</html>
```